I sell carved wood signs on line and need business cards for every order that gets mailed out
Business name- Brindlefox
Website address/ email address/ name /

```html
<!DOCTYPE html>
<html lang="en">
<head>
<meta charset="utf-8">
<title>Brindlefox Business Card</title>
<link href="https://fonts.googleapis.com/css2?family=Montserrat:wght@400;500;700&display=swap" rel="stylesheet">
<style>
  :root {
    --green: #2e9e45;
    --grey: #9a9a9a;
    --grey-light: #d4d4d4;
    --ink: #555555;
    --paper: #ffffff;
    --backdrop: #e9e9e9;
  }
  * { box-sizing: border-box; margin: 0; padding: 0; }
  html, body {
    width: 1200px; height: 900px; overflow: hidden;
    background: var(--backdrop);
    font-family: "Montserrat", sans-serif;
  }
  .canvas {
    position: relative; width: 1200px; height: 900px;
  }
  .card {
    position: absolute; left: 285px; width: 630px; height: 360px;
    background: var(--paper);
    box-shadow: 0 6px 18px rgba(0,0,0,0.12);
    overflow: hidden;
  }
  .card--front { top: 60px; }
  .card--back { top: 480px; }

  .brand-mark {
    position: absolute; display: flex; align-items: center; gap: 12px;
    color: var(--green); font-weight: 700; font-size: 34px;
  }
  .brand-mark .brand-square {
    width: 22px; height: 22px; background: var(--green);
  }
  .card--front .brand-mark { left: 50%; top: 95px; transform: translateX(-50%); }

  .front-rule {
    position: absolute; height: 2px; background: var(--grey-light);
  }
  .front-rule--left { left: 0; top: 312px; width: 190px; }
  .front-rule--right { right: 0; top: 222px; width: 170px; }
  .front-url {
    position: absolute; left: 0; right: 0; top: 258px; text-align: center;
    color: var(--green); font-weight: 700; font-size: 15px; letter-spacing: 3px;
  }
  .card-foot {
    position: absolute; left: 0; right: 0; bottom: 0; height: 12px;
    background: var(--grey-light);
  }

  .card--back .brand-mark { right: 48px; top: 40px; font-size: 30px; }
  .back-rule {
    position: absolute; left: 0; right: 0; top: 140px; height: 2px; background: var(--grey-light);
  }
  .back-brand {
    position: absolute; left: 40px; top: 92px;
    color: var(--green); font-weight: 700; font-size: 28px;
  }
  .person {
    position: absolute; left: 40px; top: 168px;
  }
  .person-accent {
    position: absolute; left: 0; top: 178px; width: 18px; height: 30px; background: var(--green);
  }
  .person-name { color: var(--green); font-weight: 700; font-size: 22px; }
  .person-role { color: var(--grey); font-size: 14px; margin-top: 2px; }
  .contact-rule {
    position: absolute; left: 0; width: 330px; top: 234px; height: 2px; background: var(--grey-light);
  }
  .contact-list {
    position: absolute; left: 40px; top: 250px; list-style: none;
    color: var(--ink); font-size: 15px;
  }
  .contact-list li { display: flex; align-items: center; gap: 10px; height: 24px; }
  .contact-list svg { width: 14px; height: 14px; fill: var(--green); }
  .address {
    position: absolute; right: 40px; top: 160px; text-align: right;
    color: var(--green); font-weight: 700; font-size: 17px; line-height: 1.3;
  }
  .address-band {
    position: absolute; right: 0; top: 236px; width: 250px; height: 24px; background: var(--green);
  }
</style>
</head>
<body>
<main class="canvas">
  <section class="card card--front">
    <div class="brand-mark"><span class="brand-square"></span>Brindlefox</div>
    <div class="front-rule front-rule--right"></div>
    <p class="front-url">www.brindlefox.com</p>
    <div class="front-rule front-rule--left"></div>
    <div class="card-foot"></div>
  </section>

  <section class="card card--back">
    <div class="brand-mark"><span class="brand-square"></span>Brindlefox</div>
    <p class="back-brand">Brindlefox</p>
    <div class="back-rule"></div>
    <div class="person-accent"></div>
    <div class="person">
      <p class="person-name">Dale Henshaw</p>
      <p class="person-role">Founder</p>
    </div>
    <div class="contact-rule"></div>
    <ul class="contact-list">
      <li><svg viewBox="0 0 16 16"><path d="M3 1l3 3-2 2c1 2 3 4 5 5l2-2 3 3-2 3C7 15 1 9 0 3z"/></svg>+001 555 0198</li>
      <li><svg viewBox="0 0 16 16"><path d="M0 3h16v10H0zM1 4l7 5 7-5v-0.5H1z" fill-rule="evenodd"/></svg>dale@brindlefox.com</li>
      <li><svg viewBox="0 0 16 16"><circle cx="8" cy="8" r="7"/></svg>www.brindlefox.com</li>
    </ul>
    <p class="address">418 Alder Hollow Lane<br>Fernvale, AK 99580</p>
    <div class="address-band"></div>
    <div class="card-foot"></div>
  </section>
</main>
</body>
</html>
```